New DermaLune logo and packaging

We would like a new design for our new product DermaLune, a high strength vitamin C serum which treats pigmentation. The packaging will reflect a high quality, clinical product with the logo "DermaLune" on the front, with it's ingredients "Vitamin C, B3, B5, E and ferulic acid" the products are in two sizes 10ml and 30ml.

This is one of many products to come out in the DermaLune range.

It would be for high end medical clinics selling premium brands, with a strong medical and clinical feel, professional and current or even futuristic in appearance.

Gold, blue, silver, White, cream are all colours that do this (without appearing cheap)

The product is not tested on animals, so would have
- "Not tested on animals".
- "12m" symbol for shelf life,
- "Made in USA"
- and ingredients list

See attached the product and existing box

Target Market(s)

Medical and aesthetic clinics

Font styles to use
Serif
Sans Serif

Colors
33a6d7
cee9f5
ffffff
fbed22
fee18a

Requirements
Must have
• High end premium brand
Nice to have
• like the idea of gold and silver lettering on cream background
Should not have
• Tacky, over complicated design

```html
<!DOCTYPE html>
<html lang="en">
<head>
<meta charset="utf-8">
<title>DermaLune Vitamin C Serum Packaging</title>
<link href="https://fonts.googleapis.com/css2?family=Oswald:wght@200;300;400&display=swap" rel="stylesheet">
<style>
  :root {
    --backdrop: #a29fa0;
    --cream: #f8f4d6;
    --cream-light: #fbf8e4;
    --gold: #c98a2a;
    --gold-light: #e8b54a;
    --ink: #2a2a2a;
    --navy: #1f3a66;
  }
  * { margin: 0; padding: 0; box-sizing: border-box; }
  html, body { width: 1200px; height: 1200px; overflow: hidden; }
  body {
    background: var(--backdrop);
    font-family: "Oswald", sans-serif;
    color: var(--ink);
    position: relative;
  }
  .box-front {
    position: absolute;
    left: 130px; top: 100px;
    width: 480px; height: 1000px;
    background: linear-gradient(180deg, var(--cream-light), var(--cream));
  }
  .brand {
    position: absolute;
    left: 0; right: 0;
    text-align: center;
    font-weight: 300;
    color: var(--gold);
    letter-spacing: 0;
    line-height: 1;
  }
  .box-front .brand { top: 236px; font-size: 92px; }
  .ingredients {
    position: absolute;
    left: 50%;
    transform: translateX(-50%);
    border: 1.5px solid var(--ink);
    white-space: nowrap;
    font-weight: 300;
    line-height: 1;
  }
  .box-front .ingredients { top: 368px; font-size: 24px; padding: 8px 12px; letter-spacing: -0.3px; }
  .volume {
    position: absolute;
    left: 0; right: 0;
    text-align: center;
    font-weight: 300;
  }
  .box-front .volume { top: 790px; font-size: 26px; }
  .gold-rule {
    position: absolute;
    left: 50%;
    transform: translateX(-50%);
    background: linear-gradient(90deg, var(--gold), var(--gold-light), var(--gold));
  }
  .box-front .gold-rule { top: 852px; width: 360px; height: 10px; }
  .claims {
    position: absolute;
    top: 900px; left: 0; right: 0;
    display: flex;
    justify-content: center;
    align-items: flex-end;
    gap: 18px;
  }
  .claim { display: flex; flex-direction: column; align-items: center; }
  .claim-label { font-size: 11px; line-height: 1.05; text-align: center; font-weight: 400; }
  .animal-icon { width: 40px; height: 30px; background: #d9d3b2; border-radius: 6px; margin-bottom: 3px; }
  .usa-badge { width: 56px; height: 56px; border-radius: 50%; background: var(--navy); }
  .bottle-label {
    position: absolute;
    left: 700px; top: 390px;
    width: 370px; height: 480px;
    background: linear-gradient(180deg, var(--cream-light), var(--cream));
  }
  .bottle-label .brand { top: 50px; font-size: 66px; }
  .bottle-label .ingredients { top: 146px; font-size: 15px; padding: 5px 8px; border-width: 1px; }
  .bottle-label .volume { top: 370px; font-size: 16px; }
  .bottle-label .gold-rule { top: 418px; width: 270px; height: 6px; }
</style>
</head>
<body>
  <section class="box-front" aria-label="30ml carton front">
    <h1 class="brand">DERMALUNE</h1>
    <p class="ingredients">VITAMIN C, B3, B5, E AND FERULIC ACID</p>
    <p class="volume">℮ &nbsp;30ML | 1FL. OZ</p>
    <div class="gold-rule"></div>
    <div class="claims">
      <div class="claim">
        <div class="animal-icon" role="img" aria-label="Rabbit icon for cruelty free"></div>
        <span class="claim-label">NOT TESTED<br>ON ANIMALS</span>
      </div>
      <div class="claim">
        <svg width="48" height="44" viewBox="0 0 48 44" aria-label="12 month shelf life">
          <path d="M6 8 L40 2" stroke="#2a2a2a" stroke-width="1.5" fill="none"/>
          <rect x="6" y="16" width="36" height="24" rx="3" fill="none" stroke="#2a2a2a" stroke-width="1.5"/>
          <line x1="6" y1="20" x2="42" y2="20" stroke="#2a2a2a" stroke-width="1.2"/>
          <text x="24" y="35" text-anchor="middle" font-family="Oswald, sans-serif" font-size="11" fill="#2a2a2a">12M</text>
        </svg>
      </div>
      <div class="claim">
        <div class="usa-badge" role="img" aria-label="Made in USA badge"></div>
      </div>
    </div>
  </section>

  <section class="bottle-label" aria-label="10ml bottle label">
    <h2 class="brand">DERMALUNE</h2>
    <p class="ingredients">VITAMIN C, B3, B5, E AND FERULIC ACID</p>
    <p class="volume">℮ &nbsp;10ML</p>
    <div class="gold-rule"></div>
  </section>
</body>
</html>
```